UI/UX Re-Do for Velmora - a free to use project management platform for desktop and mobile.

UI/UX Re-Do for Velmora
Velmora is a free to use project management platform for desktop and mobile.
We are looking for help with our UI/UX re-design.
As of now the platform is totally functional.
The problem is around flow and look. We want VM to become something that any one can use to manage and even socialize any project. A project can be something work related like organizing a team around a software build, marketing campaign, shared client file space, etc... In fact, most of our current members are using VM for just such work projects.
We also see a project as planning a wedding, organizing a group trip, a simple to-do list, organizing a kids sports team, and so on...
To become a platform that people will use in their work and personal life we first need to become more intuitive and friendly - while maintaining advanced functionality for more advanced needs.
We need help to beautify, streamline, and simplify - while keeping all the functions.
The quickest way to understand VM, and our current issues is this short video:
https://vidshare-example.net/Kq8TzRw2mLp
For sure see this link for the entire most recent description AND images:
https://velmoraapp-example.com/?p=HtrwN4YcZsD
The best way to understand VM is to actually use it:
https://velmoraapp-example.com
Should you choose to take a run at improving VM here are the details:
Please focus your ideas for mobile, it's where we have the biggest issues.
Feel free to get outside the box.
Avoid swipe oriented designs.
Feel free to focus on ideas over polished outputs.
Use any tool you like, PS, hand drawing, written description if you think that works best.
(FYI - we use mostly use Google Presentation docs internally)
Point is illustration of ideas over tool choice.
Feel free to:
Create something totally new
And/or riff on what we have now
And/or riff on the new design we are considering (see images below)
|||
If we go the direction of the images/designs below the idea is to give people options on how they see/experience VM.
Just below is what we are calling Base Mode. This is a more basic and simple flow. Probably a default to keep new users feeling comfortable at the start.
<img src="https://img.picvault-example.net/8tqWLbN.jpg" style="width: 100%;">
https://img.picvault-example.net/8tqWLbN.jpg
|||
We are calling this optional view Atlas Mode. It is more advanced and can show all project, goal(renamed 'milestones') at the same time. This is more of a paint job on the current design.
<img src="https://img.picvault-example.net/mvdHRsJ.jpg" style="width: 100%;">
https://img.picvault-example.net/mvdHRsJ.jpg
|||
If you're submitting please let us know if you can also do the PS files for dev.
Not required, but once we nail down the concepts we want someone to hone in the PS files.
As an optional bonus we will also be giving credit to you/your company in VM.
Let us know if you do or don't want that.
We are excited to see your work!!
<img src=" " style="width: 100%;">
Target Market(s)
Anyone who needs to organize any project, big or small. The key is to make a super friendly user experience for new users while retaining advanced functions.

```html
<!DOCTYPE html>
<html lang="en">
<head>
<meta charset="utf-8">
<title>Velmora – Base Mode</title>
<link href="https://fonts.googleapis.com/css2?family=Lato:wght@400;700;900&display=swap" rel="stylesheet">
<style>
:root{
  --bg:#f2f2f4;
  --white:#ffffff;
  --purple:#8c4fa6;
  --purple-card:#8e57aa;
  --orange:#f7931e;
  --red:#ef2637;
  --ink:#222226;
  --muted:#8d8d93;
  --line:#d9d9de;
  --badge:#2f8fe3;
}
*{box-sizing:border-box;margin:0;padding:0}
html,body{width:675px;height:1200px;overflow:hidden}
body{background:var(--bg);font-family:"Lato",Arial,sans-serif;color:var(--ink);position:relative}
.app-header{position:absolute;left:0;top:0;width:675px;height:153px;background:var(--white);box-shadow:0 3px 10px rgba(0,0,0,.08)}
.menu-icon{position:absolute;left:36px;top:56px}
.search{position:absolute;left:124px;top:40px;width:376px;height:64px;border:2px solid var(--line);border-radius:4px;display:flex;align-items:center;padding-left:18px;gap:16px;color:var(--muted);font-size:20px}
.search-divider{width:2px;height:36px;background:var(--line)}
.profile{position:absolute;left:538px;top:22px;width:110px;height:110px;border-radius:50%;background:linear-gradient(160deg,#c9c3bd,#6f6a68);border:4px solid var(--white);box-shadow:0 2px 8px rgba(0,0,0,.2)}
.badge{position:absolute;left:551px;top:56px;width:28px;height:28px;border-radius:50%;background:var(--badge);color:var(--white);font-size:16px;font-weight:700;display:flex;align-items:center;justify-content:center}
.section-head{position:absolute;left:58px;width:594px;display:flex;justify-content:space-between;align-items:center}
.section-title{color:var(--purple);font-size:29px;font-weight:900;letter-spacing:1px}
.section-link{color:#555;font-size:18px;font-weight:700;display:flex;align-items:center;gap:10px}
.project{position:absolute;top:261px;width:226px;height:229px;background:var(--white);box-shadow:0 4px 12px rgba(0,0,0,.12);padding:34px 22px 22px}
.project.active{background:var(--purple-card);color:var(--white)}
.project-title{font-size:20px;font-weight:900}
.project-meta{position:absolute;left:22px;right:22px;bottom:24px;display:flex;justify-content:space-between;align-items:center;font-size:20px;color:var(--muted)}
.project.active .project-meta{color:var(--white)}
.task{position:absolute;left:58px;width:599px;height:205px;background:var(--white);box-shadow:0 3px 10px rgba(0,0,0,.1);padding:24px 34px}
.task.current{background:var(--orange);color:var(--white)}
.task-top{display:flex;justify-content:space-between;align-items:center}
.task-name{font-size:20px;font-weight:900}
.task-actions{display:flex;gap:26px}
.task-body{margin-top:14px;font-size:18px;line-height:23px;color:#a9a9ae}
.task.current .task-body{color:var(--white)}
.task-foot{position:absolute;left:34px;right:34px;bottom:18px;display:flex;justify-content:space-between;align-items:center}
.stats{display:flex;gap:24px;font-size:19px;font-weight:700;color:#555}
.task.current .stats{color:var(--white)}
.stat{display:flex;align-items:center;gap:8px}
.members{display:flex;gap:6px}
.member{width:36px;height:36px;border-radius:50%;background:linear-gradient(160deg,#b9a99a,#5e5550)}
.task:not(.current) .member{opacity:.45}
.fab{position:absolute;left:540px;top:1055px;width:108px;height:108px;border-radius:50%;background:var(--red);box-shadow:0 6px 14px rgba(0,0,0,.25);display:flex;align-items:center;justify-content:center}
</style>
</head>
<body>
<header class="app-header">
  <svg class="menu-icon" width="46" height="34" viewBox="0 0 46 34" fill="#555"><rect width="46" height="4" rx="2"/><rect y="15" width="46" height="4" rx="2"/><rect y="30" width="46" height="4" rx="2"/></svg>
  <div class="search">
    <svg width="26" height="26" viewBox="0 0 26 26" fill="none" stroke="#555" stroke-width="2.5"><circle cx="15" cy="11" r="8"/><line x1="9" y1="17" x2="2" y2="24"/></svg>
    <span class="search-divider"></span>
    <span>Search</span>
  </div>
  <div class="profile" role="img" aria-label="User profile photo"></div>
  <div class="badge">5</div>
</header>

<div class="section-head" style="top:186px">
  <h2 class="section-title">PROJECTS</h2>
  <span class="section-link">See all <svg width="12" height="18" viewBox="0 0 12 18"><path d="M2 2l7 7-7 7" fill="none" stroke="#8c4fa6" stroke-width="3"/></svg></span>
</div>

<div class="project" style="left:58px">
  <div class="project-title">Project Title</div>
  <div class="project-meta"><span>12 people</span>
    <svg width="20" height="20" viewBox="0 0 20 20" fill="#b5b5ba"><path d="M2 18l1-5L14 2l4 4L7 17z"/></svg></div>
</div>
<div class="project active" style="left:311px">
  <div class="project-title">Project Title</div>
  <div class="project-meta"><span>12 people</span>
    <svg width="20" height="20" viewBox="0 0 20 20" fill="#fff"><path d="M2 18l1-5L14 2l4 4L7 17z"/></svg></div>
</div>
<div class="project" style="left:563px">
  <div class="project-title">Project Title</div>
</div>

<div class="section-head" style="top:538px">
  <h2 class="section-title">TASKS</h2>
  <span class="section-link" style="color:#777">Newest <svg width="18" height="12" viewBox="0 0 18 12"><path d="M2 2l7 7 7-7" fill="none" stroke="#8c4fa6" stroke-width="3"/></svg></span>
</div>

<article class="task current" style="top:590px">
  <div class="task-top"><span class="task-name">Task 1</span>
    <span class="task-actions">
      <svg width="22" height="22" viewBox="0 0 20 20" fill="#fff"><path d="M2 18l1-5L14 2l4 4L7 17z"/></svg>
      <svg width="24" height="22" viewBox="0 0 24 22" fill="none" stroke="#fff" stroke-width="2"><path d="M2 10L22 2l-6 18-5-7z M11 13L22 2"/></svg>
      <svg width="20" height="22" viewBox="0 0 20 22" fill="none" stroke="#fff" stroke-width="2"><path d="M2 5h16M7 5V2h6v3M4 5l1 15h10l1-15"/></svg>
    </span></div>
  <p class="task-body">Lorem ipsum dolor sit amet, consectetur adipisicing elit, sed do eiusmod tempor incididunt ut labore et dolore magna aliqua. Ut enim ad minim veniam, quis nostrud exercitation</p>
  <div class="task-foot">
    <div class="stats">
      <span class="stat"><svg width="22" height="20" viewBox="0 0 22 20" fill="none" stroke="#fff" stroke-width="2"><path d="M11 2c5 0 9 3 9 7s-4 7-9 7c-1 0-2 0-3-.3L3 18l1-4C2.8 12.6 2 11 2 9c0-4 4-7 9-7z"/></svg>12</span>
      <span class="stat"><svg width="18" height="20" viewBox="0 0 18 20" fill="none" stroke="#fff" stroke-width="2"><path d="M13 7l-6 7a2 2 0 01-3-3l7-8a3.5 3.5 0 015 5l-7 8a5 5 0 01-7-7l6-7"/></svg>5</span>
    </div>
    <div class="members">
      <span class="member" role="img" aria-label="Team member photo"></span>
      <span class="member" role="img" aria-label="Team member photo"></span>
      <span class="member" role="img" aria-label="Team member photo"></span>
      <span class="member" role="img" aria-label="Team member photo"></span>
      <span class="member" role="img" aria-label="Team member photo"></span>
      <span class="member" role="img" aria-label="Team member photo"></span>
    </div>
  </div>
</article>

<article class="task" style="top:819px">
  <div class="task-top"><span class="task-name">Task 2</span>
    <span class="task-actions">
      <svg width="22" height="22" viewBox="0 0 20 20" fill="#555"><path d="M2 18l1-5L14 2l4 4L7 17z"/></svg>
      <svg width="24" height="22" viewBox="0 0 24 22" fill="none" stroke="#555" stroke-width="2"><path d="M2 10L22 2l-6 18-5-7z M11 13L22 2"/></svg>
      <svg width="20" height="22" viewBox="0 0 20 22" fill="none" stroke="#555" stroke-width="2"><path d="M2 5h16M7 5V2h6v3M4 5l1 15h10l1-15"/></svg>
    </span></div>
  <p class="task-body">Lorem ipsum dolor sit amet, consectetur adipisicing elit, sed do eiusmod tempor incididunt ut labore et dolore magna aliqua. Ut enim ad minim veniam, quis nostrud exercitation</p>
  <div class="task-foot">
    <div class="stats">
      <span class="stat"><svg width="22" height="20" viewBox="0 0 22 20" fill="none" stroke="#555" stroke-width="2"><path d="M11 2c5 0 9 3 9 7s-4 7-9 7c-1 0-2 0-3-.3L3 18l1-4C2.8 12.6 2 11 2 9c0-4 4-7 9-7z"/></svg>12</span>
      <span class="stat"><svg width="18" height="20" viewBox="0 0 18 20" fill="none" stroke="#555" stroke-width="2"><path d="M13 7l-6 7a2 2 0 01-3-3l7-8a3.5 3.5 0 015 5l-7 8a5 5 0 01-7-7l6-7"/></svg>5</span>
    </div>
    <div class="members">
      <span class="member" role="img" aria-label="Team member photo"></span>
      <span class="member" role="img" aria-label="Team member photo"></span>
      <span class="member" role="img" aria-label="Team member photo"></span>
      <span class="member" role="img" aria-label="Team member photo"></span>
      <span class="member" role="img" aria-label="Team member photo"></span>
      <span class="member" role="img" aria-label="Team member photo"></span>
    </div>
  </div>
</article>

<article class="task" style="top:1049px">
  <div class="task-top"><span class="task-name">Task 3</span>
    <span class="task-actions">
      <svg width="22" height="22" viewBox="0 0 20 20" fill="#555"><path d="M2 18l1-5L14 2l4 4L7 17z"/></svg>
      <svg width="24" height="22" viewBox="0 0 24 22" fill="none" stroke="#555" stroke-width="2"><path d="M2 10L22 2l-6 18-5-7z M11 13L22 2"/></svg>
      <svg width="20" height="22" viewBox="0 0 20 22" fill="none" stroke="#555" stroke-width="2"><path d="M2 5h16M7 5V2h6v3M4 5l1 15h10l1-15"/></svg>
    </span></div>
  <p class="task-body">Lorem ipsum dolor sit amet, consectetur adipisicing elit, sed do eiusmod tempor incididunt ut labore et dolore magna aliqua. Ut enim ad minim veniam, quis nostrud exercitation</p>
</article>

<div class="fab" aria-label="Add new">
  <svg width="34" height="34" viewBox="0 0 34 34" stroke="#fff" stroke-width="4"><line x1="17" y1="4" x2="17" y2="30"/><line x1="4" y1="17" x2="30" y2="17"/></svg>
</div>
</body>
</html>
```